Marigolds festival band lineup and special offer flyer

Need a cool flyer for the coolest Marigolds tribute festival in the world..either 4x6 or 4x9 or both....

lots of past ideas attached

all of the current info is
www.clblk-fest.net

ext year marks the 50th Anniversary of the Autumn of Kites, when the American counter-culture became more of a lifestyle than a political choice, and the release of The Marigolds' "Cpt. Mulberry’s Quiet Riverside Dance Troupe." Cedar Lane by the Lake will feature performers popular in 1967, including Dwight Halvorsen of Gilbert’s Gadabouts, producer-singer Colin Brandt, The Tin Lanterns, The Copper Tide, and Owen Fairbank of Silas Wexford and the Nightjars.

Next year's festival will be May 25-29 and debut in its new home in Jeffersonville.

Tickets are available at www.clblk-fest.net.

Cedar Lane by the Lake averages 20,000 attendees and features around 60 performers, the majority of them Marigolds tribute bands.

Target Market(s)

Marigolds and 60's music fans

Industry/Entity Type

Festival

Font styles to use
Sans Serif
Other font styles liked:
• oswold is always cool

Colors
fbee3e
acd136
fece3e
33b8a4
33a6d7
faa54b

Requirements
Must have
• who, what, when where why
• Use Brightmoor now promo code and save $30 on Grand Passes To Wander
Nice to have
• I sent a lot of art of you to see ...we have look built around the 4 heads
Should not have
• the real marigolds or the marigolds drop t logo

```html
<!DOCTYPE html>
<html lang="en">
<head>
<meta charset="utf-8">
<title>Cedar Lane by the Lake — Jeffersonville, May 25-29 2017</title>
<link rel="stylesheet" href="https://fonts.googleapis.com/css2?family=Open+Sans:ital,wght@1,700;1,800&family=PT+Sans:wght@400&display=swap">
<style>
  :root {
    --sun: #fbce3e;
    --sun-light: #fde08a;
    --lime: #e0da12;
    --red: #e31f2b;
    --purple: #8a1a7a;
    --green: #4fa935;
    --ink: #1d1b1b;
    --white: #ffffff;
    --gold: #fcc62c;
  }
  html, body { margin: 0; padding: 0; overflow: hidden; background: #eeeeee; }
  .flyer {
    position: relative;
    width: 849px; height: 1200px;
    overflow: hidden;
    background:
      radial-gradient(circle at 40px 90px, var(--sun-light) 0 120px, transparent 121px),
      radial-gradient(circle at 790px 760px, var(--sun-light) 0 110px, transparent 111px),
      linear-gradient(to bottom, var(--sun) 0 1040px, var(--lime) 1040px);
    font-family: "PT Sans", sans-serif;
    color: var(--ink);
  }
  .event-facts {
    position: absolute; left: 24px; top: 62px; width: 300px;
    margin: 0; text-align: center;
    font-family: "Open Sans", sans-serif; font-style: italic; font-weight: 700;
    font-size: 40px; line-height: 45px; letter-spacing: -1px;
  }
  .festival-title {
    position: absolute; left: 336px; top: 52px; margin: 0;
    font-family: "Open Sans", sans-serif; font-style: italic; font-weight: 800;
    font-size: 78px; line-height: 80px; letter-spacing: -2px;
    color: var(--red);
  }
  .portraits { position: absolute; left: 38px; top: 254px; }
  .portrait { position: absolute; top: 0; width: 185px; height: 303px; }
  .portrait--green  { left: 0;   background: linear-gradient(to bottom, var(--green) 0 62%, var(--ink) 62%); }
  .portrait--red    { left: 196px; background: linear-gradient(to bottom, #c80f21 0 62%, var(--ink) 62%); }
  .portrait--purple { left: 392px; background: linear-gradient(to bottom, var(--purple) 0 62%, var(--ink) 62%); }
  .portrait--yellow { left: 588px; background: linear-gradient(to bottom, var(--gold) 0 62%, var(--ink) 62%); }
  .banner { position: absolute; }
  .banner svg { position: absolute; left: 0; top: 0; }
  .banner span {
    position: relative; display: block;
    font-family: "Open Sans", sans-serif; font-style: italic; font-weight: 800;
    color: var(--white);
  }
  .banner--concerts { left: 24px; top: 580px; width: 732px; height: 52px; }
  .banner--concerts span { padding-left: 22px; font-size: 42px; line-height: 52px; letter-spacing: -1px; }
  .lineup {
    position: absolute; left: 34px; top: 632px; width: 472px; height: 472px;
    background: var(--white); box-sizing: border-box; padding: 10px 0 0 17px;
    font-size: 23px; line-height: 24.8px; letter-spacing: -0.4px;
  }
  .lineup span { display: block; white-space: nowrap; }
  .lineup small { font-size: 16px; }
  .banner--slogan { left: 0; top: 1120px; width: 472px; height: 52px; }
  .banner--slogan span { padding-left: 44px; font-size: 40px; line-height: 52px; letter-spacing: -0.5px; }
  .promo { position: absolute; left: 568px; top: 862px; width: 240px; text-align: center; font-size: 23px; line-height: 30px; }
  .promo p { margin: 0; }
  .promo-badge {
    width: 200px; height: 172px; margin: 12px auto 10px;
    background: var(--ink); border-radius: 30px;
    font-family: "Open Sans", sans-serif; font-style: italic; font-weight: 800;
    color: var(--gold); display: flex; flex-direction: column; align-items: center; justify-content: center;
  }
  .promo-badge .save { font-size: 50px; line-height: 50px; }
  .promo-badge .amount { font-size: 88px; line-height: 90px; letter-spacing: -3px; }
</style>
</head>
<body>
<main class="flyer">
  <p class="event-facts">Jeffersonville<br>May 25-29<br>2017</p>
  <h1 class="festival-title">Cedar Lane<br>by the Lake</h1>

  <div class="portraits">
    <div class="portrait portrait--green" role="img" aria-label="Flat illustrated portrait of a band member in dark suit and tie on a green panel"></div>
    <div class="portrait portrait--red" role="img" aria-label="Flat illustrated portrait of a band member in dark suit and tie on a red panel"></div>
    <div class="portrait portrait--purple" role="img" aria-label="Flat illustrated portrait of a band member in dark suit and tie on a purple panel"></div>
    <div class="portrait portrait--yellow" role="img" aria-label="Flat illustrated portrait of a band member in dark suit and tie on a yellow panel"></div>
  </div>

  <div class="banner banner--concerts">
    <svg width="732" height="60" viewBox="0 0 732 60" aria-hidden="true">
      <polygon points="4,0 680,0 732,52 0,52" fill="var(--red)"/>
      <polygon points="0,52 12,52 12,60" fill="#9a0f18"/>
    </svg>
    <span>OVER 250 CONCERTS STARRING</span>
  </div>

  <div class="lineup">
    <span>all you want is sun • brightbeat</span>
    <span>classicslate • clube big marigolds forever</span>
    <span>maple row • gavin trell hal brennan •</span>
    <span>fiddlefern park • j.r. mcallister jay grunwald</span>
    <span>• john selwick • jukebox periscope i’s</span>
    <span>• kevin ashdale quiet riverside troupe •</span>
    <span>jan vollen qrt experience • meet the</span>
    <span>marbles megamarigolds • michael barlow</span>
    <span>nevermind the hillocks • the newbuds</span>
    <span>norwegian marigolds • peter colfax</span>
    <span>fortyseven • studio nine • starhoppers</span>
    <span>steve sandmore group • the blue</span>
    <span>drifters the blue buttons • caladrift</span>
    <span>rock band the sighers w/ steve hollins •</span>
    <span>the rowleys wilton connection • union</span>
    <span>sail yellow subterrans • long day’s</span>
    <span>light tony bramford • <small>hosted by</small> joe</span>
    <span>jameson</span>
  </div>

  <div class="banner banner--slogan">
    <svg width="472" height="52" viewBox="0 0 472 52" aria-hidden="true">
      <polygon points="0,0 420,0 472,52 0,52" fill="var(--purple)"/>
    </svg>
    <span>Flowes around me</span>
  </div>

  <section class="promo">
    <p>Use Brightmoor now<br>promo code</p>
    <div class="promo-badge"><span class="save">save</span><span class="amount">$30</span></div>
    <p>on Grand Passes<br>To Wander</p>
  </section>
</main>
</body>
</html>
```